kvt business card

need clean and modern business card design, possibly two. Logo on front and writing on back-Full source files for logo attached-THE CHOSEN LOGO IS SQUARE KVT with KVT HOLDINGS in ALL BLUE. Please do not use any other logos from files, this is source file that includes correct logo

```html
<!DOCTYPE html>
<html lang="en">
<head>
<meta charset="UTF-8">
<title>KVT Holdings Business Card</title>
<link rel="stylesheet" href="https://fonts.googleapis.com/css2?family=Roboto:wght@400;500;700&display=swap">
<style>
  :root {
    --page-bg: #2b2b2d;
    --card-bg: #0d0d0f;
    --card-edge: #1c1c1f;
    --brand-blue: #1a7fe0;
    --silver: #c9c9cc;
    --text-light: #d6d6d8;
  }
  * { margin: 0; padding: 0; box-sizing: border-box; }
  html, body {
    width: 1200px;
    height: 900px;
    overflow: hidden;
    background: var(--page-bg);
    font-family: "Roboto", Arial, sans-serif;
  }
  .stage {
    width: 1200px;
    height: 900px;
    display: flex;
    align-items: center;
    justify-content: center;
    gap: 40px;
  }
  .card {
    position: relative;
    width: 520px;
    height: 300px;
    border-radius: 22px;
    background: var(--card-bg);
    border: 1px solid var(--card-edge);
    box-shadow: 0 18px 40px rgba(0,0,0,0.45);
  }

  .brand {
    position: absolute;
    display: flex;
    flex-direction: column;
    align-items: center;
    font-weight: 500;
    letter-spacing: 0.1em;
    white-space: nowrap;
  }
  .brand-square {
    display: block;
    background: currentColor;
  }

  /* Back: contact details */
  .card-details .brand {
    top: 34px;
    left: 282px;
    width: 200px;
    color: var(--brand-blue);
    font-size: 22px;
    gap: 14px;
  }
  .card-details .brand-square { width: 50px; height: 50px; }

  .person {
    position: absolute;
    top: 128px;
    left: 40px;
  }
  .person-name {
    color: var(--brand-blue);
    font-weight: 700;
    font-size: 18px;
    letter-spacing: 0.02em;
  }
  .person-title {
    color: var(--text-light);
    font-size: 14px;
    margin-top: 2px;
  }
  .address {
    position: absolute;
    top: 176px;
    right: 40px;
    text-align: right;
    font-style: normal;
    color: var(--text-light);
    font-size: 14px;
    line-height: 1.4;
  }
  .contacts {
    position: absolute;
    left: 40px;
    bottom: 30px;
    list-style: none;
    color: var(--text-light);
    font-size: 15px;
    line-height: 1.4;
  }
  .contacts li {
    display: flex;
    align-items: center;
    gap: 8px;
  }
  .contacts svg {
    width: 12px;
    height: 12px;
    fill: var(--brand-blue);
    flex: none;
  }

  /* Front: brand only */
  .card-front .brand {
    top: 50%;
    left: 50%;
    transform: translate(-50%, -50%);
    color: var(--silver);
    font-size: 30px;
    gap: 22px;
  }
  .card-front .brand-square { width: 64px; height: 64px; }
</style>
</head>
<body>
<main class="stage">
  <section class="card card-details" aria-label="Card back with contact details">
    <div class="brand"><span class="brand-square"></span>KVT HOLDINGS</div>

    <div class="person">
      <p class="person-name">DARIA VOSSEN</p>
      <p class="person-title">Managing Director</p>
    </div>

    <address class="address">
      88, Harlow Street West<br>
      Fenbridge, 30917
    </address>

    <ul class="contacts">
      <li>
        <svg viewBox="0 0 12 12" aria-hidden="true"><path d="M1 4c0-2 2-3 3-3l1 2.5-1.3 1c.6 1.3 1.5 2.2 2.8 2.8l1-1.3L10 7c0 1-1 3-3 3C4 10 1 7 1 4z"/></svg>
        222 639 4170
      </li>
      <li>
        <svg viewBox="0 0 12 12" aria-hidden="true"><path d="M1 3h10v6H1z M1 3l5 3.5L11 3" stroke="#0d0d0f" stroke-width="0.8"/></svg>
        info@kvtgroup.net
      </li>
      <li>
        <svg viewBox="0 0 12 12" aria-hidden="true"><circle cx="6" cy="6" r="5"/><path d="M1 6h10M6 1c-2 3-2 7 0 10M6 1c2 3 2 7 0 10" stroke="#0d0d0f" stroke-width="0.8" fill="none"/></svg>
        www.kvtgroup.net
      </li>
    </ul>
  </section>

  <section class="card card-front" aria-label="Card front with company name">
    <div class="brand"><span class="brand-square"></span>KVT HOLDINGS</div>
  </section>
</main>
</body>
</html>
```